Design a 1 mobile profile page for social personal feedback app

Project name is Glimmer you.
I need a 1 mobile profile page
In this page I want show the likes and dislikes of a person.

There are multi categories on this such as
A)
Doing Sports.
Going out
Reading
Eating
Talking about
Watching
Dreaming about
Having fun
Spending money

b)
Angry if.
Love to
Believe in.
Afraid of
Proud of
Laughing to

c) Hero

Design the page with more icons and gifs .
The page has also picture .age ,gender ,where

```html
<!DOCTYPE html>
<html lang="en">
<head>
<meta charset="utf-8">
<title>Profile</title>
<link rel="stylesheet" href="https://fonts.googleapis.com/css2?family=PT+Sans:wght@400;700&display=swap">
<style>
  :root {
    --magenta: #b0249c;
    --magenta-deep: #8b1788;
    --magenta-soft: #c04aae;
    --plum-text: #a0228f;
    --chip-border: #d9d9d9;
    --white: #ffffff;
    --page-bg: #f4f1f5;
  }
  * { box-sizing: border-box; margin: 0; padding: 0; }
  html, body {
    width: 871px; height: 1200px; overflow: hidden;
    background: var(--page-bg);
    font-family: "PT Sans", Arial, sans-serif;
  }
  .screen {
    position: absolute; left: 166px; top: 25px;
    width: 540px; height: 1150px;
    background: var(--white);
    border-radius: 44px;
    overflow: hidden;
  }
  .header-art { position: absolute; left: 0; top: 0; width: 540px; height: 310px; }
  .menu-button { position: absolute; left: 13px; top: 42px; width: 48px; height: 34px; }
  .vote-button {
    position: absolute; left: 464px; width: 53px; height: 52px;
    background: var(--white); border-radius: 9px;
    display: flex; align-items: center; justify-content: center;
  }
  .vote-like { top: 153px; }
  .vote-dislike { top: 225px; }
  .avatar {
    position: absolute; left: 174px; top: 116px; width: 182px; height: 182px;
    border-radius: 50%; border: 4px solid var(--white);
    background: radial-gradient(circle at 50% 42%, #c79b7f 0%, #8f6a55 38%, #3f4a4c 70%, #9fb4b2 100%);
  }
  .status-dot {
    position: absolute; left: 312px; top: 260px; width: 24px; height: 24px;
    border-radius: 50%; background: var(--magenta-deep); border: 3px solid var(--white);
  }
  .user-name {
    position: absolute; left: 0; width: 540px; top: 306px; text-align: center;
    font-size: 42px; font-weight: 700; color: var(--plum-text); line-height: 1.1;
  }
  .user-gender {
    position: absolute; left: 0; width: 540px; top: 362px; text-align: center;
    font-size: 20px; font-weight: 700; color: var(--plum-text);
  }
  .meta-item { position: absolute; top: 397px; display: flex; align-items: center; gap: 22px; }
  .meta-location { left: 53px; }
  .meta-age { left: 314px; }
  .meta-icon {
    width: 50px; height: 50px; border-radius: 10px; background: var(--magenta);
    display: flex; align-items: center; justify-content: center;
  }
  .meta-label { font-size: 20px; font-weight: 700; color: var(--plum-text); }
  .tabs { position: absolute; left: 0; top: 474px; width: 540px; height: 72px; }
  .tab {
    position: absolute; top: 0; height: 68px;
    border: 2px solid var(--magenta); background: var(--white);
    display: flex; align-items: center; justify-content: center;
    font-size: 31px; font-weight: 700; color: var(--plum-text);
  }
  .tab-activities { left: 5px; width: 167px; background: var(--magenta); color: var(--white); border-radius: 34px 0 0 0; }
  .tab-feelings { left: 176px; width: 185px; }
  .tab-heroes { left: 366px; width: 165px; border-radius: 0 40px 0 0; }
  .tabs-rule { position: absolute; left: 5px; top: 70px; width: 526px; height: 2px; background: var(--magenta); }
  .chip {
    position: absolute; height: 54px; margin-top: -27px;
    border: 2px solid var(--chip-border); border-radius: 16px; background: var(--white);
    display: flex; align-items: center; justify-content: center; gap: 10px;
    font-size: 25px; color: var(--plum-text); white-space: nowrap;
  }
  .chip-icon { width: 34px; height: 34px; border-radius: 8px; flex: none; }
  .footer-art { position: absolute; left: 0; top: 1000px; width: 540px; height: 150px; }
  .footer-button {
    position: absolute; top: 1033px; width: 72px; height: 72px; border-radius: 50%;
    border: 4px solid var(--white); display: flex; align-items: center; justify-content: center;
  }
  .footer-settings { left: 23px; }
  .footer-power { left: 443px; }
  .home-indicator { position: absolute; left: 136px; top: 1134px; width: 259px; height: 5px; border-radius: 3px; background: var(--white); }
</style>
</head>
<body>
<main class="screen">
  <svg class="header-art" viewBox="0 0 540 310" aria-hidden="true">
    <defs>
      <linearGradient id="headerFill" x1="0" y1="0" x2="1" y2="1">
        <stop offset="0" stop-color="#b5259e"/>
        <stop offset="1" stop-color="#86178a"/>
      </linearGradient>
    </defs>
    <path d="M0 0H540V300C500 260 455 268 420 282C380 298 356 270 330 262C300 252 285 258 268 262C230 270 215 250 185 256C140 266 110 300 60 295C30 292 12 285 0 282Z" fill="url(#headerFill)"/>
    <circle cx="130" cy="40" r="110" fill="#9b1d8f" opacity=".55"/>
    <circle cx="370" cy="130" r="95" fill="#a72599" opacity=".6"/>
    <circle cx="10" cy="200" r="80" fill="#a12496" opacity=".6"/>
    <circle cx="510" cy="50" r="75" fill="#9a1b8f" opacity=".6"/>
    <circle cx="520" cy="270" r="60" fill="#c35db5" opacity=".55"/>
  </svg>

  <svg class="menu-button" viewBox="0 0 48 34" aria-label="Menu">
    <rect x="0" y="0" width="48" height="5" rx="2.5" fill="#fff"/>
    <rect x="0" y="14" width="40" height="5" rx="2.5" fill="#fff"/>
    <rect x="0" y="28" width="30" height="5" rx="2.5" fill="#fff"/>
  </svg>

  <div class="vote-button vote-like" aria-label="Like">
    <svg width="34" height="34" viewBox="0 0 24 24"><path d="M2 10h4v12H2zM8 21V10l5-8c1.5 0 2.5 1 2 3l-1 4h6c1.5 0 2.3 1.3 2 2.5l-2 8c-.3 1-1 1.5-2 1.5z" fill="#9b1d8f"/></svg>
  </div>
  <div class="vote-button vote-dislike" aria-label="Dislike">
    <svg width="34" height="34" viewBox="0 0 24 24"><path d="M2 2h4v12H2zM8 3v11l5 8c1.5 0 2.5-1 2-3l-1-4h6c1.5 0 2.3-1.3 2-2.5l-2-8C19.7 3.5 19 3 18 3z" fill="none" stroke="#9b1d8f" stroke-width="1.8"/></svg>
  </div>

  <div class="avatar" role="img" aria-label="Profile photo of the user"></div>
  <div class="status-dot"></div>

  <h1 class="user-name">User Name</h1>
  <p class="user-gender">User Gender</p>

  <div class="meta-item meta-location">
    <span class="meta-icon"><svg width="26" height="30" viewBox="0 0 24 28"><path d="M12 0C5.5 0 1 4.8 1 10.5 1 18 12 28 12 28s11-10 11-17.5C23 4.8 18.5 0 12 0z" fill="#fff"/><circle cx="12" cy="10.5" r="4" fill="#b0249c"/></svg></span>
    <span class="meta-label">User Location</span>
  </div>
  <div class="meta-item meta-age">
    <span class="meta-icon"><svg width="28" height="30" viewBox="0 0 24 26"><circle cx="12" cy="7" r="6" fill="#fff"/><path d="M1 26c0-7 5-11 11-11s11 4 11 11z" fill="#fff"/></svg></span>
    <span class="meta-label">User Age</span>
  </div>

  <nav class="tabs">
    <div class="tab tab-activities">Activitys</div>
    <div class="tab tab-feelings">Feelings</div>
    <div class="tab tab-heroes">Heros</div>
    <div class="tabs-rule"></div>
  </nav>

  <section class="activity-list">
    <div class="chip" style="left:36px;top:631px;width:229px"><span class="chip-icon" role="img" aria-label="Sports icon" style="background:#e05252"></span>Doing Sports</div>
    <div class="chip" style="left:307px;top:631px;width:191px"><span class="chip-icon" role="img" aria-label="Going out icon" style="background:#3f6fb5"></span>Going out</div>
    <div class="chip" style="left:49px;top:707px;width:167px"><span class="chip-icon" role="img" aria-label="Reading icon" style="background:#5b8fd1"></span>Reading</div>
    <div class="chip" style="left:270px;top:707px;width:212px"><span class="chip-icon" role="img" aria-label="Eating icon" style="background:#d59a5a"></span>Eating Food</div>
    <div class="chip" style="left:39px;top:783px;width:226px"><span class="chip-icon" role="img" aria-label="Talking icon" style="background:#7fa7cf"></span>Talking about</div>
    <div class="chip" style="left:317px;top:783px;width:179px"><span class="chip-icon" role="img" aria-label="Watching icon" style="background:#4c7dbd"></span>Watching</div>
    <div class="chip" style="left:35px;top:857px;width:259px"><span class="chip-icon" role="img" aria-label="Dreaming icon" style="background:#9a6bc4"></span>Dreaming about</div>
    <div class="chip" style="left:307px;top:857px;width:191px"><span class="chip-icon" role="img" aria-label="Fun icon" style="background:#e8b557"></span>Having fun</div>
    <div class="chip" style="left:131px;top:938px;width:270px"><span class="chip-icon" role="img" aria-label="Money icon" style="background:#6a4fb0;border-radius:50%"></span>Spending money</div>
  </section>

  <svg class="footer-art" viewBox="0 0 540 150" aria-hidden="true">
    <defs>
      <linearGradient id="footerFill" x1="0" y1="0" x2="0" y2="1">
        <stop offset="0" stop-color="#b5259e"/>
        <stop offset="1" stop-color="#8c178a"/>
      </linearGradient>
    </defs>
    <path d="M0 10C120 -2 200 20 300 14C400 8 470 2 540 12V150H0Z" fill="url(#footerFill)"/>
  </svg>

  <div class="footer-button footer-settings" aria-label="Settings">
    <svg width="44" height="44" viewBox="0 0 24 24"><path d="M10 1h4l.6 3 2.2 1.3 2.9-1 2 3.4-2.3 2 0 2.6 2.3 2-2 3.4-2.9-1-2.2 1.3-.6 3h-4l-.6-3-2.2-1.3-2.9 1-2-3.4 2.3-2v-2.6l-2.3-2 2-3.4 2.9 1L9.4 4z" fill="#fff"/><circle cx="12" cy="12" r="3.6" fill="#9d1e91"/></svg>
  </div>
  <div class="footer-button footer-power" aria-label="Log out">
    <svg width="40" height="40" viewBox="0 0 24 24"><path d="M7 5.5A8.5 8.5 0 1 0 17 5.5" fill="none" stroke="#fff" stroke-width="2.8" stroke-linecap="round"/><path d="M12 2v9" stroke="#fff" stroke-width="2.8" stroke-linecap="round"/></svg>
  </div>
  <div class="home-indicator"></div>
</main>
</body>
</html>
```